Modern solo law firm website

I am preparing to launch a solo law practice (I own the domain farrowcounsel.com and/or may use Farrow Law Office as a dba), and will need to move quickly to put up a website once I pull the trigger. There are many existing law firm sites to "copy," but I'm looking for something a little more modern and unique with some scrolling and modern icons (see e.g., brintelaw.com). Right now, need the logo and skeleton for the site, as I have not written all of the content. For now, I like the idea of a simple home page that incorporates the phrase "Impactful. Valuable. Trusted." (Again, I may change that text.) And would like links on the home page across the top for "about", "services", "people" and "contact" -- these should lead to separate landing pages. The bottom of the home page also should have a link for a "disclaimer" and to Facebook, Twitter and LinkedIn (which I have not yet created). Make sense? Let me know if you have questions.

Target Market(s)

Business clients

Industry/Entity Type

Law Firm

Number of Pages Required

5+ page

Font styles to use
Other font styles liked:
• Perhaps Segoe UI

Requirements
Must have
• DRAFT STRUCTURE AND TEXT NOW ATTACHED. HOWEVER, SUBJECT TO EDITS BEING MADE CONCURRENTLY.

```html
<!DOCTYPE html>
<html lang="en">
<head>
<meta charset="utf-8">
<title>Farrow Legal – Law Practice</title>
<link href="https://fonts.googleapis.com/css2?family=Open+Sans:wght@400;600;700&family=Roboto+Condensed:wght@400;700&family=Handlee&display=swap" rel="stylesheet">
<style>
:root{
  --blue:#1a9bd7;
  --blue-dark:#0f7fb5;
  --ink:#333;
  --muted:#8a8a8a;
  --line:#ececec;
  --dark:#1f1f1f;
  --footer:#3a3a3a;
  --footer-bottom:#222;
  --white:#fff;
}
*{margin:0;padding:0;box-sizing:border-box}
html,body{width:706px;height:1200px;overflow:hidden;background:var(--white)}
body{font-family:"Open Sans",sans-serif;color:var(--ink);position:relative}
.page{position:relative;width:706px;height:1200px;overflow:hidden}

/* header */
.site-header{position:absolute;top:0;left:0;width:706px;height:64px;background:var(--white)}
.brand{position:absolute;left:100px;top:16px;display:flex;align-items:center;gap:9px}
.brand-dot{width:30px;height:30px;border-radius:50%;background:var(--blue)}
.brand-name{font-family:"Open Sans",sans-serif;font-weight:700;font-size:21px;color:var(--blue)}
.main-nav a{position:absolute;top:27px;font-size:9.5px;color:#555;text-decoration:none;white-space:nowrap}
.social-top{position:absolute;left:565px;top:28px;display:flex;gap:3px}
.social-top span{width:10px;height:10px;border-radius:50%;background:var(--blue)}

/* hero */
.hero{position:absolute;top:64px;left:0;width:706px;height:300px;
  background:linear-gradient(100deg,#d8cfc6 0%,#b79a7c 22%,#6e4a2f 45%,#4a2a18 65%,#3a2316 100%)}
.hero-arrow{position:absolute;top:140px;width:18px;height:18px;border-radius:50%;background:rgba(0,0,0,.55);display:flex;align-items:center;justify-content:center}
.hero-arrow.prev{left:34px}.hero-arrow.next{left:658px}
.hero-copy{position:absolute;left:389px;top:44px;width:270px;color:var(--white)}
.hero-title{font-family:"Roboto Condensed",sans-serif;font-weight:700;font-size:36px;line-height:42px}
.hero-sub{font-family:"Roboto Condensed",sans-serif;font-size:26px;line-height:34px;margin-top:4px}
.hero-text{font-size:8px;line-height:12.5px;margin-top:22px;width:258px}
.btn{display:inline-block;background:var(--blue);color:var(--white);font-size:8.5px;text-transform:uppercase;padding:6px 10px;border-radius:2px;text-decoration:none}
.hero .btn{margin-top:18px}

/* welcome */
.welcome{position:absolute;top:378px;left:100px;width:506px;text-align:center}
.welcome h1{font-weight:400;font-size:21px;color:#333}
.welcome h1 b{font-weight:400;color:var(--blue)}
.welcome p{font-size:6.2px;line-height:10px;color:var(--muted);margin-top:8px}

/* services */
.services{position:absolute;top:470px;left:100px;width:506px;height:190px}
.services .divider-v{position:absolute;left:253px;top:0;width:1px;height:190px;background:var(--line)}
.services .divider-h{position:absolute;left:0;top:95px;width:506px;height:1px;background:var(--line)}
.service{position:absolute;width:245px;height:90px}
.service-icon{position:absolute;left:0;top:10px;width:42px;height:42px;border-radius:50%;border:1px solid var(--line);display:flex;align-items:center;justify-content:center}
.service h3{position:absolute;left:73px;top:10px;font-weight:400;font-size:10.5px;color:#333;white-space:nowrap}
.service p{position:absolute;left:73px;top:30px;width:168px;font-size:6.5px;line-height:10.5px;color:var(--muted)}

/* impact band */
.impact{position:absolute;top:675px;left:0;width:706px;height:194px;
  background:linear-gradient(90deg,#2a1e16 0%,#1a1411 50%,#120e0c 100%)}
.video{position:absolute;left:100px;top:20px;width:228px;height:148px;border:2px solid #5a4a3a;
  background:linear-gradient(120deg,#c2a27a,#7a5230 55%,#3a2416)}
.video .play{position:absolute;left:84px;top:44px;width:54px;height:54px;border-radius:50%;border:4px solid rgba(255,255,255,.9);background:rgba(0,0,0,.25)}
.video .bar{position:absolute;left:0;bottom:0;width:100%;height:10px;background:rgba(0,0,0,.7)}
.video .bar i{position:absolute;left:8px;top:4px;width:120px;height:2px;background:var(--blue)}
.impact-copy{position:absolute;left:347px;top:18px;width:262px;color:var(--white)}
.impact-copy h2{font-weight:600;font-size:18px}
.impact-copy .lead{font-size:10px;margin-top:5px}
.impact-copy p.body{font-size:6.8px;line-height:11px;color:#ddd;margin-top:10px}
.impact .btn{margin-top:10px;font-size:9.5px;text-transform:none;padding:6px 14px}

/* people */
.people{position:absolute;top:892px;left:100px;width:506px;height:190px}
.person{position:absolute;top:0;width:157px;height:190px;background:#fafafa;border:1px solid var(--line);text-align:center}
.person-photo{width:72px;height:72px;border-radius:50%;margin:12px auto 0;
  background:linear-gradient(180deg,#d9d4cf,#9aa3b0 60%,#394250)}
.person h4{font-family:"Handlee",cursive;font-weight:400;font-size:14px;color:var(--blue);margin-top:12px}
.person p{font-size:6.3px;line-height:10px;color:var(--muted);width:118px;margin:6px auto 0}
.person .shares{display:flex;justify-content:center;gap:8px;margin-top:14px}
.person .shares span{width:6px;height:6px;border-radius:50%;background:#999}

/* footer */
.site-footer{position:absolute;top:1103px;left:0;width:706px;height:64px;background:var(--footer)}
.site-footer .brand{left:100px;top:17px}
.site-footer .brand-name{color:var(--white)}
.footer-address,.footer-contact{position:absolute;top:17px;font-size:9.5px;line-height:15px;color:var(--white);font-style:normal}
.footer-address{left:296px}.footer-contact{left:417px}
.site-footer .btn{position:absolute;left:538px;top:21px;text-transform:none;font-size:9px;padding:6px 11px;border-radius:10px}
.bottom-bar{position:absolute;top:1167px;left:0;width:706px;height:33px;background:var(--footer-bottom)}
.bottom-bar small{position:absolute;left:100px;top:13px;font-size:6px;color:#999}
.bottom-bar .social{position:absolute;left:541px;top:8px;display:flex;gap:4px}
.bottom-bar .social span{width:17px;height:17px;border-radius:50%;border:1px solid #aaa}
.bottom-bar .disclaimer{position:absolute;left:606px;top:13px;font-size:6px;color:#999;text-decoration:none}
</style>
</head>
<body>
<div class="page">

  <header class="site-header">
    <div class="brand"><span class="brand-dot"></span><span class="brand-name">Farrow Legal</span></div>
    <nav class="main-nav">
      <a href="#" style="left:312px">Home</a>
      <a href="#" style="left:359px">About</a>
      <a href="#" style="left:405px">Services</a>
      <a href="#" style="left:459px">People</a>
      <a href="#" style="left:509px">Contact</a>
    </nav>
    <div class="social-top"><span></span><span></span><span></span></div>
  </header>

  <section class="hero" role="img" aria-label="Photograph of brass scales of justice in a wood-panelled courtroom">
    <span class="hero-arrow prev"><svg width="8" height="8" viewBox="0 0 8 8"><path d="M5 1L2 4l3 3" stroke="#fff" stroke-width="1.4" fill="none"/></svg></span>
    <span class="hero-arrow next"><svg width="8" height="8" viewBox="0 0 8 8"><path d="M3 1l3 3-3 3" stroke="#fff" stroke-width="1.4" fill="none"/></svg></span>
    <div class="hero-copy">
      <div class="hero-title">Farrow Legal</div>
      <div class="hero-sub">Law Practise</div>
      <p class="hero-text">Big Law plays an important part in the legal services industry. While you get the resources of a large organization, the services are costly and mis-incentivized as your lawyers benefit from taking longer and charging every</p>
      <a class="btn" href="#">Get to know us</a>
    </div>
  </section>

  <section class="welcome">
    <h1>Welcome To <b>Farrow Legal</b></h1>
    <p>Farrow Legal was founded in 2014 by Alan Farrow who has been helping clients solve their legal problems since 1996. Farrow Legal is dedicated to helping mature companies, small and medium-size businesses, and start-ups alike obtain superior results from their outside counsel at prices they find valuable. Impactful. Valuable. Trusted. How does one generate superior results at a great value? Alan Farrow believes it starts with being a good listener.</p>
  </section>

  <section class="services">
    <span class="divider-v"></span><span class="divider-h"></span>
    <article class="service" style="left:0;top:0">
      <span class="service-icon"><svg width="22" height="18" viewBox="0 0 22 18" fill="#1a9bd7"><circle cx="6" cy="5" r="3"/><circle cx="16" cy="5" r="3"/><circle cx="11" cy="7" r="3.4"/><path d="M1 16c0-4 3-6 5-6s3 1 3 1-3 2-3 5zM21 16c0-4-3-6-5-6s-3 1-3 1 3 2 3 5zM5 18c0-5 3-7 6-7s6 2 6 7z"/></svg></span>
      <h3>Outside General Counsel</h3>
      <p>Maybe you have an in-house counsel, or maybe you don't. Farrow Legal can provide you with the in-house counsel services your company needs so your employees can focus on their primary jobs.</p>
    </article>
    <article class="service" style="left:270px;top:0">
      <span class="service-icon"><svg width="22" height="20" viewBox="0 0 22 20" fill="none" stroke="#1a9bd7" stroke-width="1.4"><path d="M11 2v16M6 18h10M3 5h16M3 5l-2.5 6h5zM19 5l-2.5 6h5z"/></svg></span>
      <h3>Litigation and Dispute Resolution</h3>
      <p>Maybe you have an in-house counsel, or maybe you don't. Farrow Legal can provide you with the in-house counsel services your company needs so your employees can focus on their primary jobs.</p>
    </article>
    <article class="service" style="left:0;top:100px">
      <span class="service-icon"><svg width="20" height="20" viewBox="0 0 20 20" fill="#1a9bd7"><circle cx="10" cy="4" r="3"/><path d="M5 11c0-3 2-4 5-4s5 1 5 4z"/><rect x="3" y="11" width="14" height="8"/></svg></span>
      <h3>Employment Consulting</h3>
      <p>Maybe you have an in-house counsel, or maybe you don't. Farrow Legal can provide you with the in-house counsel services your company needs so your employees can focus on their primary jobs.</p>
    </article>
    <article class="service" style="left:270px;top:100px">
      <span class="service-icon"><svg width="16" height="20" viewBox="0 0 16 20" fill="none" stroke="#1a9bd7" stroke-width="1.4"><rect x="1" y="1" width="14" height="18"/><path d="M4 6h8M4 9h8M4 12h8M4 15h5"/></svg></span>
      <h3>Business Documents</h3>
      <p>Maybe you have an in-house counsel, or maybe you don't. Farrow Legal can provide you with the in-house counsel services your company needs so your employees can focus on their primary jobs.</p>
    </article>
  </section>

  <section class="impact">
    <div class="video" role="img" aria-label="Video still of scales of justice on a desk">
      <span class="play"><svg width="46" height="46" viewBox="0 0 46 46"><path d="M18 13l14 10-14 10z" fill="#fff"/></svg></span>
      <span class="bar"><i></i></span>
    </div>
    <div class="impact-copy">
      <h2>Impactful. Valuable. Trusted</h2>
      <p class="lead">That's how you should think of your lawyers, right?</p>
      <p class="body">Big Law plays an important part in the legal services industry. While you get the resources of a large organization, the services are costly and mis-incentivized as your lawyers benefit from taking longer and charging every angle, regardless of whether it makes the most sense for your needs and budget. Even there, smart that. Farrow Legal is committed to making your life easier. To explore and listen to your true needs. To provide simple explanations.</p>
      <a class="btn" href="#">Watch the video</a>
    </div>
  </section>

  <section class="people">
    <article class="person" style="left:0">
      <div class="person-photo" role="img" aria-label="Portrait photo of a team member"></div>
      <h4>Mark Ellison</h4>
      <p>Mr. Farrow is licensed to practice law in Illinois and is a member of the trial bar for the Northern District of Illinois</p>
      <div class="shares"><span></span><span></span><span></span></div>
    </article>
    <article class="person" style="left:174px">
      <div class="person-photo" role="img" aria-label="Portrait photo of a team member"></div>
      <h4>Mark Ellison</h4>
      <p>Mr. Farrow is licensed to practice law in Illinois and is a member of the trial bar for the Northern District of Illinois</p>
      <div class="shares"><span></span><span></span><span></span></div>
    </article>
    <article class="person" style="left:349px">
      <div class="person-photo" role="img" aria-label="Portrait photo of a team member"></div>
      <h4>Mark Ellison</h4>
      <p>Mr. Farrow is licensed to practice law in Illinois and is a member of the trial bar for the Northern District of Illinois</p>
      <div class="shares"><span></span><span></span><span></span></div>
    </article>
  </section>

  <footer class="site-footer">
    <div class="brand"><span class="brand-dot"></span><span class="brand-name">Farrow Legal</span></div>
    <address class="footer-address">418 Linden Ave.<br>Marlow, IL 60299</address>
    <div class="footer-contact">555-014-2290<br>info@farrowcounsel.com</div>
    <a class="btn" href="#">Get in Touch</a>
  </footer>
  <div class="bottom-bar">
    <small>© 2013 - 2014 · Farrow Legal. All Rights Reserved.</small>
    <div class="social"><span></span><span></span><span></span></div>
    <a class="disclaimer" href="#">Disclaimer</a>
  </div>

</div>
</body>
</html>
```